Website for 9 year old artist, helps animal rescue charity :)

I am looking to have a simple website created for my 9 year old son's small "company." He makes necklaces and art out of beachcombed treasures and sells them for animal rescue charity. Currently, his domain name www.gullcovepebblecraft.com brings people straight to his friendvine page, but for those who are not on FV, nothing shows up.

I would like a simple landing page + a few other clickable pages that will show his logo (already done by Pixel Assembly folks!) +
* photos
* a brief description about what he does
* a link to the charities he supports
* link to his Friendvine Page (https://www.friendvine.com/GullCovePebblecraft)
* are where a link to a possible craftly store could go (future, we haven't gotten that far). :)
(really just a "shop" button)
I need to be able to add and remove photos and text, add calendar dates of events he will be at, and adjust links if needed.

I hope this isn't too complicated! It doesn't need to be flashy, just an easy on the eyes page where people who are interested in his necklaces and his charity work can go to find out more. I would like to have the website incorporate the two logos (see uploads). I image the image of the child beachcombing being on the bottom anchoring the page, but that is as far as my imagination has gone regarding the web design! :)

UPDATED:
Name of web url: www.gullcovepebblecraft.com
Name of company: Gull Cove Pebblecraft
Purpose: Milo is 9 years old. He beachcombs with his family all over the United States and finds wonderful shells, seaglass, and pottery. His mom helps him drill the holes in these piece and then he creates one of a kind necklaces using these beachcombed treasures and silver charms. He also makes sweet shell, seaglass and driftwood angels (Milo's Cherubs). All shells are responsibly collected. Every piece is designed by Milo.

At least 20% off all proceeds from every sale goes to animal rescue charity.

Target Market(s)

The target market for his necklaces is typically women, but we have a lot of guys buy them, too, to hang in their windows or to give away. All ages of folks buy his necklaces at the small sales and fairs we have gone to. They also look at his site to find out more about Willow Paws Cat Rescue, the organization Milo donates a lot of his proceeds to.

We get a lot of requests about whether he has a webpage and find that many of the people who want to check it out do not have Friendvine, so linking right to FV hasn't worked.

Industry/Entity Type

Charity

Requirements
Must have
• * Logos (I have 2 done by design works folks). The one of the beachcombing child is for the website only, the one of the shell angel will be for the website and business cards, etc.
* Spaces for photos
* Clickable links to Friendvine, Craftly (later), charity(s) he donates to
* Space for Bio/backstory
* Contact us area

Match the blues of the two logos so they are the same shade.

The look should be young and simple, without being childish. We are beachcombers at heart, so sea and sand colors would work great. All blues (except electric), greens, tans, etc are great.

I added a ton of images for reference. Please message me if you would like more.
Nice to have
• * Area I can add the tally of how much he has donated so far
* Slideshow of images (I uploaded a ton for examples)
* Page dedicated to images and information about the of the rescue organization he primarily donates to. The rescue organization is dedicated to the rehabilitation and adoption of special needs and abused cats.
Should not have
• Curlz font or anything too cutesy

Bright colors, I am hoping for a more muted, seas-inspired look.

```html
<!DOCTYPE html>
<html lang="en">
<head>
<meta charset="utf-8">
<title>Gull Cove Pebblecraft</title>
<link href="https://fonts.googleapis.com/css2?family=Bree+Serif&family=Open+Sans:wght@400;600;700&display=swap" rel="stylesheet">
<style>
  :root {
    --bar-dark: #2a2a2a;
    --nav-dark: #333333;
    --sand: #dcd8cc;
    --sea-blue: #4cb9d2;
    --white: #ffffff;
    --muted: #b9b9b9;
    --ink: #080808;
    --cell-dark: #141414;
    --cell-line: #3a3a3a;
  }
  * { margin: 0; padding: 0; box-sizing: border-box; }
  html, body { width: 1200px; height: 680px; overflow: hidden; background: var(--white); }
  body { position: relative; font-family: "Open Sans", Arial, sans-serif; }

  .topbar { position: absolute; left: 0; top: 0; width: 1200px; height: 52px; background: var(--bar-dark); border-top: 2px solid #3d4a55; z-index: 2; }
  .contact { position: absolute; left: 167px; top: 15px; font-size: 8.5px; color: var(--muted); line-height: 16px; }
  .contact svg { width: 7px; height: 8px; vertical-align: -1px; margin-right: 2px; fill: var(--muted); }
  .contact .mail { margin-left: 7px; }
  .social { position: absolute; left: 722px; top: 19px; display: flex; gap: 16px; }
  .social span { width: 7px; height: 7px; border-radius: 50%; background: #d8d8d8; display: block; }
  .cart { position: absolute; left: 913px; top: 0; width: 85px; height: 58px; background: var(--white); color: var(--sea-blue); font-size: 9px; font-weight: 600; text-align: center; }
  .cart .label { margin-top: 17px; display: flex; justify-content: center; align-items: center; gap: 6px; line-height: 12px; }
  .cart .label svg { width: 13px; height: 11px; fill: var(--sea-blue); }
  .cart .count { margin-top: 10px; font-size: 9.5px; line-height: 12px; }

  .header { position: absolute; left: 0; top: 52px; width: 1200px; height: 118px; background: var(--sand); }
  .logo-art { position: absolute; left: 176px; top: 5px; width: 46px; height: 106px; background: linear-gradient(180deg, rgba(76,185,210,0.25), rgba(76,185,210,0.6)); }
  .brand { position: absolute; left: 272px; top: 31px; font-family: "Bree Serif", Georgia, serif; font-size: 23.5px; color: var(--sea-blue); white-space: nowrap; }

  .event { position: absolute; left: 593px; top: 34px; width: 405px; height: 43px; display: flex; background: var(--cell-dark); }
  .event-title { width: 183px; height: 100%; background: repeating-linear-gradient(135deg, #222 0 2px, #161616 2px 4px); font-family: "Bree Serif", Georgia, serif; color: var(--sea-blue); font-size: 17px; display: flex; align-items: center; justify-content: center; }
  .cell { height: 100%; border-left: 1px solid var(--cell-line); color: var(--white); text-align: center; display: flex; flex-direction: column; justify-content: center; }
  .cell b { font-size: 16px; font-weight: 700; line-height: 16px; }
  .cell small { font-size: 10.5px; line-height: 12px; }
  .event-more { width: 25px; background: var(--sea-blue); color: var(--white); font-size: 14px; display: flex; align-items: center; justify-content: center; }

  .nav { position: absolute; left: 0; top: 170px; width: 1200px; height: 41px; background: var(--nav-dark); }
  .nav ul { position: absolute; left: 177px; top: 15px; list-style: none; display: flex; gap: 20px; }
  .nav li { font-size: 8.8px; font-weight: 600; color: var(--white); }
  .search { position: absolute; left: 852px; top: 10px; width: 146px; height: 26px; background: #2b2b2b; }
  .search svg { position: absolute; right: 5px; top: 9px; width: 8px; height: 8px; }

  .hero { position: absolute; left: 0; top: 211px; width: 1200px; height: 469px; background: radial-gradient(ellipse at 45% 25%, #8a7668 0%, #6f665d 30%, #8f8b85 60%, #5f5a55 100%); }
  .message { position: absolute; left: 158px; top: 226px; width: 588px; height: 207px; background: var(--ink); padding: 18px 20px; font-family: "Bree Serif", Georgia, serif; color: var(--sea-blue); }
  .message h1 { font-weight: 400; font-size: 68px; line-height: 78px; white-space: nowrap; }
  .message p { font-size: 28px; margin-top: 8px; white-space: nowrap; }
</style>
</head>
<body>
  <div class="topbar">
    <div class="contact">
      <div><svg viewBox="0 0 10 12"><path d="M5 0a4 4 0 0 0-4 4c0 3 4 8 4 8s4-5 4-8a4 4 0 0 0-4-4zm0 5.5A1.5 1.5 0 1 1 5 2.5a1.5 1.5 0 0 1 0 3z"/></svg>12 Tidewater Lane, Portland, USA</div>
      <div><svg viewBox="0 0 8 12"><rect x="0" y="0" width="8" height="12" rx="1"/></svg>+00 55 218 47 90<span class="mail"><svg viewBox="0 0 12 9"><path d="M0 0h12v9H0zM1 1l5 4 5-4"/></svg>hello@gullcovepebblecraft.com</span></div>
    </div>
    <div class="social"><span></span><span></span><span></span><span></span><span></span><span></span></div>
    <div class="cart">
      <div class="label"><svg viewBox="0 0 14 12"><path d="M0 0h3l1 2h10l-2 6H5L3 1H0zM5 10a1 1 0 1 0 0 2 1 1 0 0 0 0-2zm6 0a1 1 0 1 0 0 2 1 1 0 0 0 0-2z"/></svg>Cart</div>
      <div class="count">2&nbsp; items</div>
    </div>
  </div>

  <div class="header">
    <div class="logo-art" role="img" aria-label="Logo illustration of a child beachcombing along the shore"></div>
    <div class="brand">Gull Cove Pebblecraft</div>
    <div class="event">
      <div class="event-title">Upcoming Event</div>
      <div class="cell" style="width:42px"><b>465</b><small>Days</small></div>
      <div class="cell" style="width:42px"><b>9</b><small>Hours</small></div>
      <div class="cell" style="width:58px"><b>0</b><small>Minutes</small></div>
      <div class="cell" style="width:55px"><b>56</b><small>Seconds</small></div>
      <div class="event-more">+</div>
    </div>
  </div>

  <nav class="nav">
    <ul>
      <li>HOME</li><li>ABOUT</li><li>BLOG</li><li>CHARITY EVENTS</li><li>CHARITY STORE</li><li>GALLERY</li><li>FEATURES</li><li>CROWDFUNDING</li><li>CONTACT</li>
    </ul>
    <div class="search"><svg viewBox="0 0 10 10"><circle cx="4" cy="4" r="3" fill="none" stroke="#ddd" stroke-width="1.6"/><path d="M6.2 6.2L9.3 9.3" stroke="#ddd" stroke-width="1.6"/></svg></div>
  </nav>

  <section class="hero" role="img" aria-label="Close-up photo of beach pebbles, shell fragments and a blue-patterned pottery shard in sand">
    <div class="message">
      <h1>Big, Bold Message</h1>
      <p>With a subtitle and more information</p>
    </div>
  </section>
</body>
</html>
```